Home Automation Company needs DL size flyer design

We need a flyer that looks like a home control touch panel page on a smartphone. Similar to a "Homevia9" home page. The company is Based in Sydney and named "Allwovenin". We integrate home systems into one central control. Lights, Power, Audio/Visual, Cameras, Security, Access Control, Media Storage. We are inviting people to have their future home now. Looking at new company Logo similar to "Threaded Journal"

Target Market(s)

Home Owners Eastern Suburbs Sydney

Industry/Entity Type

Home Improvement

Contact Information for Business Card

Possibly mini Smartphone look like flyer.

Font styles to use
Other font styles liked:
• TP Black Extended

Colors
cadf82
ffffff
86cfc6
f59195

Requirements
Must have
• A few Media Streaming Services Logos
• Promote ease of use and lifestyle enhancement.
• Security of Home, "Peace of mind" focus.
Nice to have
• Pictures of "Press buttons for services available"
• Home control in one app. remote access from anywere.

```html
<!DOCTYPE html>
<html lang="en">
<head>
<meta charset="utf-8">
<title>Allwovenin – Evolve Your Home Now</title>
<link rel="stylesheet" href="https://fonts.googleapis.com/css2?family=Jost:wght@300;400;500&display=swap">
<style>
  :root{
    --mauve:#9a6f6c;
    --olive:#93ad40;
    --leaf:#6f9b34;
    --forest:#2e6b1f;
    --tan:#9a7b5c;
    --ink:#4f4f4f;
    --grey:#6c6c6c;
    --white:#ffffff;
    --bubble:rgba(140,110,92,.55);
    --partner:#858585;
  }
  *{margin:0;padding:0;box-sizing:border-box}
  html,body{width:927px;height:1200px;overflow:hidden;background:#f2f0ee}
  body{font-family:"Jost",sans-serif}
  .flyer{position:relative;width:927px;height:1200px;overflow:hidden}
  .backdrop{
    position:absolute;inset:0;
    background:
      radial-gradient(ellipse 320px 420px at 640px 880px, rgba(226,186,160,.75), transparent 70%),
      radial-gradient(ellipse 380px 520px at 900px 800px, rgba(214,150,176,.75), transparent 75%),
      radial-gradient(ellipse 420px 380px at 200px 1050px, rgba(190,170,150,.55), transparent 75%),
      radial-gradient(ellipse 360px 260px at 330px 420px, rgba(222,210,170,.6), transparent 75%),
      linear-gradient(180deg,#f1f0ef 0%,#ebe6df 40%,#dec9c2 75%,#cfa9b0 100%);
  }
  .handset{
    position:absolute;left:552px;top:452px;width:250px;height:536px;border-radius:34px;
    background:linear-gradient(180deg,#cfd2d4 0%,#b9bcb6 30%,#8c9677 55%,#5f8a3c 80%,#1d1d1d 100%);
    opacity:.9;
  }
  .headline{position:absolute;left:38px;top:58px;font-weight:400;font-size:66px;line-height:70px;letter-spacing:-1px}
  .headline .w1{color:var(--mauve)}
  .headline .w2{color:var(--olive)}
  .headline .w3{color:var(--forest)}
  .headline .w4{color:var(--tan)}
  .headline .w5{color:var(--leaf)}
  .tagline{position:absolute;left:37px;top:200px;font-weight:300;font-size:28px;letter-spacing:1.5px;color:var(--grey)}
  .services-title{position:absolute;left:33px;top:307px;font-weight:400;font-size:20px;color:var(--ink)}
  .services{position:absolute;left:33px;top:361px;width:420px;list-style:none;font-weight:400;font-size:17.5px;line-height:21.5px;color:var(--ink)}
  .services li{position:relative;padding-left:21px;margin-bottom:12.5px}
  .services li::before{content:"";position:absolute;left:2px;top:9px;width:5px;height:5px;border-radius:50%;background:var(--ink)}
  .feature{position:absolute;width:120px;height:120px;margin:-60px 0 0 -60px;border-radius:50%;background:var(--bubble);display:flex;align-items:center;justify-content:center}
  .feature svg{width:64px;height:64px}
  .label{position:absolute;transform:translateX(-50%);font-weight:400;font-size:13.5px;letter-spacing:1.3px;color:var(--white);white-space:nowrap}
  .brand{position:absolute;left:48px;top:1126px;display:flex;align-items:center;gap:14px}
  .brand-mark{width:22px;height:22px;border-radius:50%;background:var(--white)}
  .brand-name{font-weight:400;font-size:29px;letter-spacing:-.5px;color:var(--white);border-top:2px solid var(--white);border-bottom:2px solid var(--white);padding:2px 2px 0}
  .partners{position:absolute;top:1150px;font-weight:500;font-size:15px;letter-spacing:1px;color:var(--partner)}
</style>
</head>
<body>
<main class="flyer">
  <div class="backdrop" role="img" aria-label="Soft-focus photo of a two-storey suburban house with hands holding a smartphone showing the home control app"></div>
  <div class="handset" role="img" aria-label="Smartphone screen showing a house photo on the app home screen"></div>

  <h1 class="headline">
    <span class="w1">EVOLVE</span> <span class="w2">YOUR HOME</span> <span class="w3">NOW</span><br>
    <span class="w4">AND BE</span> <span class="w5">CONNECTED</span>
  </h1>
  <p class="tagline">REMOTE ACCESS FROM ANYWERE</p>

  <h2 class="services-title">SERVICES INCLUDING</h2>
  <ul class="services">
    <li>Main/Sub Boards and Automation (smart home) controllers.</li>
    <li>Telephone, Data/Internet setup, TV, CCTV, Intercom/PABX</li>
    <li>Home theatre, multi room audio, sources central or local Speakers.</li>
    <li style="width:290px">Multi room, music or video in any or all room flexibility. Coupled with high quality audio and HD video.</li>
    <li style="width:330px">Touch Panels (in wall or wireless), Monitors, OLED, LCD, LED Televisions</li>
    <li>Movement detectors for lighting, flood lighting.</li>
    <li>Stainless/Glass/Stone power and light switches.</li>
    <li>Alarm systems, detectors</li>
    <li style="width:330px">CCTV Camera styles. Indoor/Outdoor IP/analogue</li>
    <li style="width:280px">Windows, Awnings, Blinds control (wind rain sensors)</li>
    <li style="width:280px">Light fittings, LED lighting, specifications and design.</li>
    <li>Risers and cabling access.</li>
    <li>Floor heating, Air Conditioning</li>
  </ul>

  <div class="feature" style="left:752px;top:416px">
    <svg viewBox="0 0 64 64" fill="#fff"><circle cx="20" cy="17" r="9" fill="none" stroke="#fff" stroke-width="4"/><circle cx="40" cy="19" r="7" fill="none" stroke="#fff" stroke-width="4"/><rect x="8" y="30" width="38" height="22" rx="3"/><path d="M46 40l12-8v20l-12-8z"/></svg>
  </div>
  <span class="label" style="left:750px;top:486px">CAMERAS</span>

  <div class="feature" style="left:520px;top:462px">
    <svg viewBox="0 0 64 64" fill="#fff"><rect x="18" y="6" width="6" height="16"/><rect x="40" y="6" width="6" height="16"/><path d="M12 22h40v10c0 10-8 16-14 16v12H26V48c-6 0-14-6-14-16z"/></svg>
  </div>
  <span class="label" style="left:520px;top:534px">POWER</span>

  <div class="feature" style="left:408px;top:578px">
    <svg viewBox="0 0 64 64" fill="#fff"><path d="M32 4c-12 0-20 9-20 19 0 8 6 12 8 20h24c2-8 8-12 8-20 0-10-8-19-20-19z"/><rect x="21" y="46" width="22" height="4" rx="2"/><rect x="21" y="52" width="22" height="4" rx="2"/><rect x="25" y="58" width="14" height="4" rx="2"/></svg>
  </div>
  <span class="label" style="left:408px;top:648px">LIGHTS</span>

  <div class="feature" style="left:816px;top:636px">
    <svg viewBox="0 0 64 64" fill="#fff"><rect x="8" y="4" width="48" height="14" rx="4"/><rect x="8" y="22" width="48" height="14" rx="4"/><rect x="29" y="36" width="6" height="14"/><rect x="8" y="50" width="48" height="4"/><circle cx="32" cy="52" r="6"/></svg>
  </div>
  <span class="label" style="left:820px;top:704px">MEDIA STORAGE</span>

  <div class="feature" style="left:390px;top:860px">
    <svg viewBox="0 0 64 64" fill="#fff"><path d="M32 6L4 30h8v28h40V30h8z"/><circle cx="26" cy="36" r="6" fill="#8c6e5c"/><path d="M30 39l14 10-2 3-3-2-2 3-3-2 2-3-8-6z" fill="#8c6e5c"/></svg>
  </div>
  <span class="label" style="left:392px;top:922px">ACCESS CONTROL</span>

  <div class="feature" style="left:532px;top:900px">
    <svg viewBox="0 0 64 64" fill="#fff"><path d="M20 28V18a12 12 0 0 1 24 0v10h-6V18a6 6 0 0 0-12 0v10z"/><rect x="12" y="28" width="40" height="32" rx="3"/><circle cx="32" cy="41" r="4" fill="#8c6e5c"/><rect x="30" y="43" width="4" height="9" fill="#8c6e5c"/></svg>
  </div>
  <span class="label" style="left:528px;top:970px">SECURITY</span>

  <div class="feature" style="left:828px;top:924px">
    <svg viewBox="0 0 64 64" fill="#fff"><path d="M26 10L2 32h7v24h34V32h7z"/><path d="M20 36l12 7-12 7z" fill="#8c6e5c"/><path d="M46 12v30a8 8 0 1 1-4-7V8l14 4v8z"/></svg>
  </div>
  <span class="label" style="left:828px;top:996px">AUDIO/VISUAL</span>

  <div class="brand">
    <span class="brand-mark"></span>
    <span class="brand-name">ALLWOVENIN</span>
  </div>

  <span class="partners" style="left:400px">LUMORA</span>
  <span class="partners" style="left:520px">TUNEWELL</span>
  <span class="partners" style="left:612px">EBBLINE</span>
  <span class="partners" style="left:724px">SONGPOST</span>
  <span class="partners" style="left:826px">DIALWAVE</span>
</main>
</body>
</html>
```